Corporate branding needed for startup digital consulting business

Startup consulting company "fenrix consulting" specialising in digital consulting in the areas of Information management, social media, digital marketing and investment strategies.

Design needs to be simple, stylish and sophisticated, bold and engaging. It should convey growth and prosperity.

The following is required:
1. Business Logo
2. Business card (2 sided) - with usual details such as phone, website, etc.
3. Letterhead
4. Powerpoint template

Let me know if you need any more information.

Target Market(s)

Business Owners, MD, Head of Technology, Marketing Directors

Industry/Entity Type

Internet

Font styles to use
Sans Serif

Requirements
Must have
• Design needs to be simple, stylish and sophisticated, bold and engaging. It should convey growth and prosperity.
Nice to have
• Looking for earthy colours like blue, olive, oranges on black or white
Should not have
• no pink

```html
<!DOCTYPE html>
<html lang="en">
<head>
<meta charset="utf-8">
<title>fenrix consulting – stationery</title>
<link href="https://fonts.googleapis.com/css2?family=Mulish:wght@400;600;700&display=swap" rel="stylesheet">
<style>
  :root {
    --backdrop: #c6c6c6;
    --paper: #ffffff;
    --brand-blue: #0a5d9e;
    --brand-orange: #f7941e;
    --ink: #1d1d1d;
    --ghost: #eeeeee;
    --rule: #f2c27a;
  }
  * { margin: 0; padding: 0; box-sizing: border-box; }
  html, body { width: 1200px; height: 1000px; overflow: hidden; }
  body {
    background: var(--backdrop);
    font-family: "Mulish", sans-serif;
    color: var(--ink);
    position: relative;
  }
  .sheet { position: absolute; background: var(--paper); overflow: hidden; }
  .band { position: absolute; left: 0; bottom: 0; width: 100%; }

  /* business card back (contact side) */
  .card-contact { left: 112px; top: 284px; width: 339px; height: 209px; }
  .card-contact .mark-square {
    position: absolute; left: 28px; top: 120px; width: 52px; height: 52px;
    background: var(--brand-orange); border-radius: 6px;
  }
  .card-contact .person { position: absolute; left: 171px; top: 22px; }
  .person-name { color: var(--brand-orange); font-weight: 700; font-size: 13px; }
  .person-role { font-size: 8px; margin-top: 4px; }
  .contact-list { position: absolute; left: 171px; top: 84px; font-size: 10px; line-height: 13px; }
  .contact-list .row { display: flex; align-items: center; gap: 5px; }
  .contact-list .gap { height: 8px; }
  .contact-list .address { margin-top: 8px; font-size: 9.5px; line-height: 12px; }
  .icon { width: 8px; height: 8px; flex: none; }

  /* business card front (brand side) */
  .card-brand { left: 112px; top: 557px; width: 339px; height: 210px; }
  .brand-lockup {
    position: absolute; left: 0; top: 96px; width: 100%;
    display: flex; justify-content: center; align-items: center; gap: 10px;
  }
  .brand-lockup .dot { width: 22px; height: 22px; background: var(--brand-orange); border-radius: 4px; }
  .brand-name { color: var(--brand-blue); font-weight: 700; font-size: 27px; letter-spacing: 0.5px; }

  /* letterhead */
  .letterhead { left: 531px; top: 95px; width: 585px; height: 826px; }
  .letterhead .brand-lockup {
    left: 50px; top: 50px; width: auto; justify-content: flex-start; gap: 7px;
  }
  .letterhead .brand-lockup .dot { width: 20px; height: 20px; }
  .letterhead .brand-name { font-size: 20px; }
  .letterhead-contact {
    position: absolute; left: 435px; top: 22px; padding-left: 6px;
    border-left: 1px solid var(--rule); font-size: 7px; line-height: 9px;
  }
  .letterhead-contact .row { display: flex; align-items: center; gap: 3px; }
  .letterhead-contact .icon { width: 6px; height: 6px; }
  .letterhead-contact .address { margin-top: 3px; }
  .ghost-square {
    position: absolute; left: 331px; top: 635px; width: 136px; height: 134px;
    background: var(--ghost); border-radius: 12px;
  }
</style>
</head>
<body>

<section class="sheet card-contact">
  <div class="mark-square"></div>
  <div class="person">
    <div class="person-name">Marta Quinlan</div>
    <div class="person-role">Director</div>
  </div>
  <div class="contact-list">
    <div class="row">
      <svg class="icon" viewBox="0 0 8 8"><rect x="2" y="0.5" width="4" height="7" rx="0.8" fill="none" stroke="#0a5d9e" stroke-width="1"/></svg>
      <span>+971 6 4400000</span>
    </div>
    <div class="row">
      <svg class="icon" viewBox="0 0 8 8"><path d="M0.5 3 Q4 0 7.5 3 L6.5 4 L5.5 3 L2.5 3 L1.5 4 Z M1.5 4.5 H6.5 V7.5 H1.5 Z" fill="#0a5d9e"/></svg>
      <span>+971 6 2283940</span>
    </div>
    <div class="gap"></div>
    <div class="row">
      <svg class="icon" viewBox="0 0 8 8"><rect x="0.5" y="1.5" width="7" height="5" fill="#0a5d9e"/><path d="M0.5 1.5 L4 4.5 L7.5 1.5" fill="none" stroke="#fff" stroke-width="0.7"/></svg>
      <span>info@dalvenmotors.com</span>
    </div>
    <div class="row">
      <svg class="icon" viewBox="0 0 8 8"><circle cx="4" cy="4" r="3.4" fill="none" stroke="#0a5d9e" stroke-width="0.9"/><path d="M0.6 4 H7.4 M4 0.6 Q2 4 4 7.4 M4 0.6 Q6 4 4 7.4" fill="none" stroke="#0a5d9e" stroke-width="0.6"/></svg>
      <span>www.dalvenmotors.com</span>
    </div>
    <div class="address">14 Acacia Road, Eros Park,<br>Windhoek, Namibia, 9000</div>
  </div>
  <svg class="band" width="339" height="18" viewBox="0 0 339 18">
    <polygon points="0,0 108,0 112,18 0,18" fill="var(--brand-blue)"/>
    <polygon points="115,0 339,0 339,18 119,18" fill="var(--brand-orange)"/>
  </svg>
</section>

<section class="sheet card-brand">
  <div class="brand-lockup">
    <div class="dot"></div>
    <div class="brand-name">fenrix consulting</div>
  </div>
  <svg class="band" width="339" height="19" viewBox="0 0 339 19">
    <polygon points="0,0 110,0 114,19 0,19" fill="var(--brand-blue)"/>
    <polygon points="117,0 339,0 339,19 121,19" fill="var(--brand-orange)"/>
  </svg>
</section>

<section class="sheet letterhead">
  <div class="brand-lockup">
    <div class="dot"></div>
    <div class="brand-name">fenrix consulting</div>
  </div>
  <div class="letterhead-contact">
    <div class="row">
      <svg class="icon" viewBox="0 0 8 8"><path d="M0.5 3 Q4 0 7.5 3 L6.5 4 L5.5 3 L2.5 3 L1.5 4 Z M1.5 4.5 H6.5 V7.5 H1.5 Z" fill="#0a5d9e"/></svg>
      <span>+123 555 0148</span>
    </div>
    <div class="row">
      <svg class="icon" viewBox="0 0 8 8"><rect x="0.5" y="1.5" width="7" height="5" fill="#0a5d9e"/></svg>
      <span>info@fenrixconsulting.com</span>
    </div>
    <div class="row">
      <svg class="icon" viewBox="0 0 8 8"><circle cx="4" cy="4" r="3.4" fill="none" stroke="#0a5d9e" stroke-width="1"/></svg>
      <span>www.fenrixconsulting.com</span>
    </div>
    <div class="address">8 Harbour Lane, Eros Park<br>City Name, Australia 9000</div>
  </div>
  <div class="ghost-square"></div>
  <svg class="band" width="585" height="24" viewBox="0 0 585 24">
    <polygon points="0,0 187,0 191,24 0,24" fill="var(--brand-blue)"/>
    <polygon points="196,0 585,0 585,24 200,24" fill="var(--brand-orange)"/>
  </svg>
</section>

</body>
</html>
```